Criação de Papelaria (6 itens) para Lumiar & Castelo
A empresa queria:
" EMPRESA FAMILIAR PRODUTORA DE GRÃOS hA 34 ANOS NO MERCADO, PIONEIRA EM IRRIGAÇÃO TIPO PIVO CENTRAL. "

```html
<!DOCTYPE html>
<html lang="pt-BR">
<head>
<meta charset="UTF-8">
<title>Lumiar &amp; Castelo — Envelope Saco</title>
<link rel="stylesheet" href="https://fonts.googleapis.com/css2?family=Cormorant+Garamond:wght@500&family=Lato:wght@400&display=swap">
<style>
  :root {
    --bg: #ececea;
    --paper: #ffffff;
    --gold: #b99453;
    --gold-light: #d2b77f;
    --taupe: #6f665d;
    --ink: #6f665d;
    --faint: #f1eeee;
    --faint-dark: #7a7168;
  }
  * { box-sizing: border-box; margin: 0; padding: 0; }
  html, body { width: 1200px; height: 1200px; overflow: hidden; }
  body {
    background: var(--bg);
    position: relative;
    font-family: "Lato", sans-serif;
  }
  .envelope {
    position: absolute;
    top: 230px;
    width: 500px;
    height: 720px;
    overflow: hidden;
    box-shadow: 0 6px 22px rgba(0,0,0,0.12);
  }
  .envelope--front { left: 70px; background: var(--paper); }
  .envelope--back { left: 630px; background: var(--taupe); }

  .envelope__flap {
    position: absolute; top: 0; left: 0; right: 0; height: 62px;
    background: linear-gradient(180deg, var(--gold-light), var(--gold));
  }
  .envelope__edge {
    position: absolute; top: 0; bottom: 0; left: 0; width: 8px;
    background: var(--gold);
  }
  .envelope__decor {
    position: absolute; border-radius: 50%;
  }
  .envelope--front .envelope__decor {
    width: 380px; height: 380px; left: 110px; top: 150px;
    background: var(--faint);
  }
  .envelope--back .envelope__decor {
    width: 420px; height: 420px; left: -40px; top: 220px;
    background: var(--faint-dark);
  }

  .brand {
    position: absolute;
    display: flex; align-items: center; gap: 14px;
  }
  .brand__dot {
    width: 30px; height: 30px; border-radius: 50%;
    background: var(--gold);
    flex: none;
  }
  .brand__name {
    font-family: "Cormorant Garamond", serif;
    font-weight: 500;
    font-size: 40px;
    line-height: 1.0;
  }
  .envelope--front .brand { left: 58px; top: 230px; }
  .envelope--front .brand__name { color: var(--ink); }
  .envelope--back .brand { left: 150px; top: 300px; }
  .envelope--back .brand__name { color: #ffffff; }

  .contact {
    position: absolute; right: 34px; bottom: 44px;
    list-style: none;
    display: flex; flex-direction: column; gap: 7px;
  }
  .contact__item {
    display: flex; align-items: center; justify-content: flex-end; gap: 9px;
    font-size: 11px; color: var(--ink);
  }
  .contact__icon {
    width: 18px; height: 18px; background: var(--gold);
    display: flex; align-items: center; justify-content: center;
  }
  .contact__icon svg { width: 12px; height: 12px; }
</style>
</head>
<body>

<section class="envelope envelope--front" aria-label="Frente do envelope saco">
  <div class="envelope__flap"></div>
  <div class="envelope__edge"></div>
  <div class="envelope__decor"></div>
  <div class="brand">
    <span class="brand__dot"></span>
    <span class="brand__name">Lumiar &amp;<br>Castelo</span>
  </div>
  <ul class="contact">
    <li class="contact__item">(00) 3000-4000
      <span class="contact__icon"><svg viewBox="0 0 24 24" fill="#fff"><path d="M6.6 10.8a15 15 0 0 0 6.6 6.6l2.2-2.2a1 1 0 0 1 1-.25 11 11 0 0 0 3.6.6 1 1 0 0 1 1 1V20a1 1 0 0 1-1 1A17 17 0 0 1 3 4a1 1 0 0 1 1-1h3.5a1 1 0 0 1 1 1 11 11 0 0 0 .6 3.6 1 1 0 0 1-.25 1z"/></svg></span>
    </li>
    <li class="contact__item">contato@lumiarcastelo.com
      <span class="contact__icon"><svg viewBox="0 0 24 24" fill="none" stroke="#fff" stroke-width="2"><rect x="3" y="6" width="18" height="12"/><path d="M3 6l9 7 9-7"/></svg></span>
    </li>
    <li class="contact__item">www.lumiarcastelo.com
      <span class="contact__icon"><svg viewBox="0 0 24 24" fill="none" stroke="#fff" stroke-width="2"><circle cx="12" cy="12" r="9"/><path d="M3 12h18M12 3c3 3 3 15 0 18M12 3c-3 3-3 15 0 18"/></svg></span>
    </li>
    <li class="contact__item">Rodovia Velha, km 12
      <span class="contact__icon"><svg viewBox="0 0 24 24" fill="#fff"><path d="M12 2a7 7 0 0 0-7 7c0 5 7 13 7 13s7-8 7-13a7 7 0 0 0-7-7zm0 9.5A2.5 2.5 0 1 1 12 6.5a2.5 2.5 0 0 1 0 5z"/></svg></span>
    </li>
  </ul>
</section>

<section class="envelope envelope--back" aria-label="Verso do envelope saco">
  <div class="envelope__decor"></div>
  <div class="brand">
    <span class="brand__dot"></span>
    <span class="brand__name">Lumiar &amp;<br>Castelo</span>
  </div>
</section>

</body>
</html>
```